Northfield Heritage Construction & Affiliates Redesigning our Look

We need stationary (letterhead, envelopes, notepads, invoicing templates, etc) that all coordinate. We are an commerial and residential exteriors construction company that operates 3 companies which all run exclusively, however, the compliment one another well.

Northfield Heritage Construction (this company installs exteriors on jobsites both residential and commercial)
Northfield Heritage Roofing & Building Supply (this company sells exterior building materials to homeowners and builders.)
Northfield Heritage Dumpster Services (This company delivers roll away dumpster cans to homeowners and builders)

Just a note: When I say we do exterior work. We do roofing, siding, stone, windows/doors, gutters, and decks.

We are looking for stationary that includes all three and keeps with our patriotic theme

Info on our firm:
Address: 2719 Tamsworth Rd, Larkmoor OR 97999
Phone: 555-555-0187
Website: www.northfieldheritage.example

Target Market(s)

Our companies target market is vast. We work in the B2B space as well as with homeowner (retail customers). We are in the home and commercial buiding construction field. We specialized in exteriors. (Roofing, Siding, Stone, Windows, Doors, Decks, Gutters)

Industry/Entity Type

Construction

Colors
ec1f27
ffffff
0555a3

Requirements
Must have
• Would like to have a clean professional look with a patriotic theme
Nice to have
• Red/White/Blue

```html
<!DOCTYPE html>
<html lang="en">
<head>
<meta charset="UTF-8">
<title>Northfield Heritage Letterhead</title>
<link href="https://fonts.googleapis.com/css2?family=Oswald:wght@500&family=Open+Sans:wght@400&display=swap" rel="stylesheet">
<style>
  :root {
    --backdrop: #e9e9ea;
    --paper: #ffffff;
    --navy: #1d2055;
    --red: #e3212a;
    --ink: #16161c;
    --footer-ink: #2b2d45;
  }
  html, body {
    margin: 0;
    padding: 0;
    width: 1200px;
    height: 1062px;
    overflow: hidden;
    background: var(--backdrop);
  }
  .letterhead {
    position: absolute;
    left: 220px;
    top: 39px;
    width: 760px;
    height: 984px;
    background: var(--paper);
    box-shadow: 0 2px 6px rgba(0,0,0,0.12);
    overflow: hidden;
  }
  .corner {
    position: absolute;
    width: 170px;
    height: 150px;
  }
  .corner--top-left { left: 0; top: 0; }
  .corner--bottom-right { right: 0; bottom: 0; }
  .brand {
    position: absolute;
    left: 78px;
    top: 58px;
    display: flex;
    align-items: center;
    gap: 12px;
  }
  .brand__mark {
    width: 14px;
    height: 14px;
    background: var(--red);
    flex: none;
  }
  .brand__name {
    font-family: 'Oswald', sans-serif;
    font-weight: 500;
    font-size: 30px;
    line-height: 1.05;
    color: var(--ink);
    letter-spacing: 0.2px;
  }
  .contact {
    position: absolute;
    right: 74px;
    bottom: 48px;
    text-align: right;
    font-family: 'Open Sans', sans-serif;
    font-size: 10.5px;
    color: var(--footer-ink);
    line-height: 1.7;
    white-space: nowrap;
  }
  .contact__line { display: flex; justify-content: flex-end; align-items: center; gap: 12px; }
  .contact__item { display: inline-flex; align-items: center; gap: 4px; }
  .contact__icon { width: 10px; height: 10px; fill: var(--navy); flex: none; }
</style>
</head>
<body>
  <main class="letterhead">
    <svg class="corner corner--top-left" viewBox="0 0 170 150" aria-hidden="true">
      <polygon points="0,0 170,0 158,9 9,9 9,138 0,150" fill="var(--navy)"/>
    </svg>

    <div class="brand">
      <span class="brand__mark"></span>
      <span class="brand__name">Northfield Heritage<br>Roofing &amp; Building Supply</span>
    </div>

    <footer class="contact">
      <div class="contact__line">2719 Tamsworth Rd, Larkmoor OR 97999</div>
      <div class="contact__line">
        <span class="contact__item">
          <svg class="contact__icon" viewBox="0 0 10 10" aria-hidden="true"><path d="M2 1h2l1 2.5-1.3 1a5 5 0 0 0 2 2L6.5 5 9 6v2a1 1 0 0 1-1 1A8 8 0 0 1 1 2a1 1 0 0 1 1-1z"/></svg>
          555-555-0187
        </span>
        <span class="contact__item">
          <svg class="contact__icon" viewBox="0 0 10 10" aria-hidden="true"><path d="M0 2h10v6H0z M0.8 2.6 5 5.6 9.2 2.6" stroke="#fff" stroke-width="0.8"/></svg>
          info@nhaffiliates.example
        </span>
        <span class="contact__item">
          <svg class="contact__icon" viewBox="0 0 10 10" aria-hidden="true"><circle cx="5" cy="5" r="4.5"/><path d="M0.5 5h9M5 0.5v9M5 0.5c-2.5 2.5-2.5 6.5 0 9M5 0.5c2.5 2.5 2.5 6.5 0 9" stroke="#fff" stroke-width="0.6" fill="none"/></svg>
          www.northfieldheritage.example
        </span>
      </div>
    </footer>

    <svg class="corner corner--bottom-right" viewBox="0 0 170 150" aria-hidden="true">
      <polygon points="170,150 0,150 12,141 161,141 161,12 170,0" fill="var(--red)"/>
    </svg>
  </main>
</body>
</html>
```